Plakate LANTERNHALL REVUE SOIREE
LANTERNHALL REVUE SOIREE
Einen Querschnitt der besten Musicals.
Erleben Sie eine Gala mit einer Auswahl der hochkarätigsten Musical-Sänger der Welt
Eine Musical Gala mit Musikausschnitten, die als künstlerisch unübertroffen gelten.
Wer kennt sie nicht, die Musicals, wie Velmora, Morrow Glass Lantern, Orlina, Wisp, Les Vagabondes d'Arvel, The Velvet Quarry Revue, Prinz der Falken, Ninth Lantern, North Pier Ballad, Quiver, Moss und viele mehr. Lanternhall Revue Soiree zeigt das Beste aus den Musicals, die Piet Holloway, Martin Ashby Crane, Henri Lucas Verdouillet, Ambrose Feldkamp, Felix Tarrowmill, Rupert Aldwick, Dale Finch, Nils Harrowby, Emil und Otto Brackwald oder Rolf Van Tassing berühmt gemacht haben.
Die Lanternhall Revue Soiree mit ihrem edlen Touch begeistert jeden Zuschauer durch die hervorragenden Stimmen, die eleganten Kostüme und die Lichtshow. Einer der Spielorte der Tournee war die ehrwürdige Orvetta (Teatro Del Pavone) in Mailand, Publikum, Presse und TV standen Kopf. Die Lanternhall Revue Soiree erhielt ausschließlich positive Kritiken. Eine große Show und Standing Ovation. Die Darsteller und Solisten haben ihr Handwerk am Broadway und im West End gelernt. Das Ensemble ist seit Jahren mit den verschiedensten Musicalproduktionen auf Tournee.
Lanternhall Revue Soiree zeigt dem Publikum einen Querschnitt der besten Musicals. Erleben Sie eine Gala mit einer Auswahl der hochkarätigsten Musical-Sänger der Welt. Ein Ereignis, an das sich jeder Besucher noch lange erinnern wird.
Anbei sende ich Dir das alte Plakat.
Dieses ist schon Jahre alt und nicht mehr zeitgemäß.
Ich freue mich auf Vorschläge
Bitte keine KI erstellten Plakate.
Gerne offene Datei in PS oder ID

```html
<!DOCTYPE html>
<html lang="en">
<head>
<meta charset="utf-8">
<title>Lanternhall Revue Soiree – Poster</title>
<link rel="stylesheet" href="https://fonts.googleapis.com/css2?family=Cinzel:wght@400&family=Inter:wght@400;500;600&display=swap">
<style>
  :root {
    --page: #ffffff;
    --black: #050202;
    --curtain-deep: #2a0604;
    --curtain-mid: #6e1a0e;
    --curtain-glow: #a8361c;
    --gold: #f4e4c4;
    --gold-glow: rgba(255, 214, 150, 0.55);
    --white: #ffffff;
    --star: #f1d27a;
    --wood-light: #e08a3c;
    --wood-dark: #5a2410;
  }
  * { box-sizing: border-box; margin: 0; padding: 0; }
  html, body {
    width: 1200px; height: 2396px; overflow: hidden;
    background: var(--page);
  }
  .poster {
    position: absolute; left: 40px; top: 405px;
    width: 1120px; height: 1585px; overflow: hidden;
    background: var(--black);
    font-family: "Inter", Arial, sans-serif;
    color: var(--white);
  }
  .poster-backdrop {
    position: absolute; inset: 0;
    background:
      radial-gradient(ellipse 38% 42% at 50% 44%, var(--curtain-glow) 0%, var(--curtain-mid) 40%, var(--curtain-deep) 72%, transparent 100%),
      linear-gradient(180deg, #140302 0%, #3a0a06 30%, #2a0604 60%, var(--black) 92%);
  }
  .poster-floor {
    position: absolute; left: 0; right: 0; top: 1360px; height: 225px;
    background: linear-gradient(180deg, rgba(5,2,2,0) 0%, var(--black) 70%);
  }
  .organizer {
    position: absolute; top: 125px; left: 0; width: 100%;
    text-align: center; font-size: 22px; letter-spacing: 1px;
  }
  .organizer strong { font-size: 36px; font-weight: 600; letter-spacing: 0; }
  .tagline {
    position: absolute; top: 226px; left: 0; width: 100%;
    text-align: center; font-size: 32px; letter-spacing: 11px; font-weight: 400;
  }
  .event-title {
    position: absolute; top: 290px; left: 0; width: 100%;
    text-align: center; font-family: "Cinzel", "Times New Roman", serif;
    font-weight: 400; color: var(--gold);
    text-shadow: 0 0 18px var(--gold-glow), 0 0 4px rgba(255,230,190,0.6);
    line-height: 1;
  }
  .event-title .line-one { display: block; font-size: 110px; }
  .event-title .line-two { display: block; font-size: 92px; margin-top: 28px; }
  .featuring {
    position: absolute; top: 722px; left: 102px;
    font-size: 29px; font-weight: 600; line-height: 1.22;
  }
  .soloist-cities {
    position: absolute; top: 822px; left: 102px; list-style: none;
  }
  .soloist-cities li {
    font-size: 38px; font-weight: 500; height: 64px;
    display: flex; align-items: center; gap: 20px;
  }
  .soloist-cities svg { width: 22px; height: 22px; fill: var(--star); }
  .event-date {
    position: absolute; top: 1080px; left: 98px;
    font-size: 100px; font-weight: 500; letter-spacing: -2px; line-height: 1;
  }
  .event-year { position: absolute; top: 1192px; left: 110px; font-size: 32px; }
  .venue { position: absolute; top: 1258px; left: 110px; line-height: 1.1; }
  .venue-city { font-size: 33px; font-weight: 600; }
  .venue-hall { font-size: 24px; font-weight: 400; }
  .venue-time { font-size: 33px; margin-top: 12px; }
  .venue-time small { font-size: 23px; }
  .guitar-scene {
    position: absolute; left: 590px; top: 690px; width: 430px; height: 700px;
    background:
      radial-gradient(ellipse 35% 22% at 38% 72%, var(--wood-light) 0%, #b65a22 45%, rgba(90,36,16,0.6) 75%, transparent 100%),
      radial-gradient(ellipse 50% 60% at 55% 55%, rgba(90,36,16,0.35) 0%, transparent 75%);
  }
  .show-list {
    position: absolute; top: 1500px; left: 0; width: 100%;
    text-align: center; font-size: 18.5px; font-weight: 400; letter-spacing: 0.2px;
    display: flex; justify-content: center; align-items: center; gap: 9px;
    white-space: nowrap;
  }
  .show-list svg { width: 13px; height: 13px; fill: var(--star); }
</style>
</head>
<body>
<main class="poster">
  <div class="poster-backdrop" role="img" aria-label="Dark red stage curtain lit by a spotlight"></div>
  <div class="guitar-scene" role="img" aria-label="Acoustic guitar leaning against a bar stool on a spotlit stage"></div>
  <div class="poster-floor"></div>

  <p class="organizer">ORGANIZED BY <strong>LOGO</strong></p>
  <p class="tagline">THE GREATEST HITS OF ALL TIME</p>
  <h1 class="event-title">
    <span class="line-one">LANTERNHALL</span>
    <span class="line-two">REVUE SOIREE</span>
  </h1>

  <p class="featuring">FEATURING INTERNATIONAL<br>STAR SOLOISTS FROM</p>
  <ul class="soloist-cities">
    <li><svg viewBox="0 0 24 24"><path d="M12 1l3.1 7.2 7.9.7-6 5.2 1.8 7.7L12 17.8 5.2 21.8 7 14.1 1 8.9l7.9-.7z"/></svg>New York</li>
    <li><svg viewBox="0 0 24 24"><path d="M12 1l3.1 7.2 7.9.7-6 5.2 1.8 7.7L12 17.8 5.2 21.8 7 14.1 1 8.9l7.9-.7z"/></svg>London</li>
    <li><svg viewBox="0 0 24 24"><path d="M12 1l3.1 7.2 7.9.7-6 5.2 1.8 7.7L12 17.8 5.2 21.8 7 14.1 1 8.9l7.9-.7z"/></svg>Vienna</li>
  </ul>

  <p class="event-date">15.05.</p>
  <p class="event-year">2026</p>
  <div class="venue">
    <p class="venue-city">BERLIN</p>
    <p class="venue-hall">CITY CONCERT HALL</p>
    <p class="venue-time">20:00<small>UHR</small></p>
  </div>

  <p class="show-list">
    <span>LES VAGABONDES D'ARVEL</span>
    <svg viewBox="0 0 24 24"><path d="M12 1l3.1 7.2 7.9.7-6 5.2 1.8 7.7L12 17.8 5.2 21.8 7 14.1 1 8.9l7.9-.7z"/></svg>
    <span>WISP</span>
    <svg viewBox="0 0 24 24"><path d="M12 1l3.1 7.2 7.9.7-6 5.2 1.8 7.7L12 17.8 5.2 21.8 7 14.1 1 8.9l7.9-.7z"/></svg>
    <span>ORLINA</span>
    <svg viewBox="0 0 24 24"><path d="M12 1l3.1 7.2 7.9.7-6 5.2 1.8 7.7L12 17.8 5.2 21.8 7 14.1 1 8.9l7.9-.7z"/></svg>
    <span>QUIVER</span>
    <svg viewBox="0 0 24 24"><path d="M12 1l3.1 7.2 7.9.7-6 5.2 1.8 7.7L12 17.8 5.2 21.8 7 14.1 1 8.9l7.9-.7z"/></svg>
    <span>VELMORA</span>
    <svg viewBox="0 0 24 24"><path d="M12 1l3.1 7.2 7.9.7-6 5.2 1.8 7.7L12 17.8 5.2 21.8 7 14.1 1 8.9l7.9-.7z"/></svg>
    <span>THE VELVET QUARRY REVUE</span>
  </p>
</main>
</body>
</html>
```